Sales book / brochure for high end plumbing services

I'd like a brochure / sales books for my sales people to use with customers in the field. It needs to look professional, clean, and do the job of showing customers what services we offer.

I already have content, and brand colors. I'm looking for the most eye-catching and professional look we can achieve.

Size - standard A4 paper size. Number of pages can vary.

Target Market(s)

Home owners, upmarket, 30-70 years old.

Colors

Designer to choose colors to be used in the design.

Requirements
Must have
• Clear design, readability, eye catching design without being too cluttered.
• In terms of images, pictures of pipes and plumbers are fairly boring. I'd rather see lifestyle pics that create the right feeling.
Nice to have
• Company color scheme:
• Logo colors (HTML)
• Red: #C72A2B
• Dark Blue: 232755
• Light Blue: 2593d2
• Logo Colors Pantone
• Dark blue - 2695 C
• Light blue - 279 C
• Red - 186 C

```html
<!DOCTYPE html>
<html lang="en">
<head>
<meta charset="utf-8">
<title>Hard Water Brochure Spread</title>
<link rel="stylesheet" href="https://fonts.googleapis.com/css2?family=Montserrat:wght@300;400&family=Open+Sans:wght@400;600;700&family=Arimo:wght@400;700&display=swap">
<style>
  :root {
    --brand-red: #c72a2b;
    --brand-red-deep: #a91b22;
    --brand-red-dark: #8e1419;
    --brand-blue: #2593d2;
    --brand-navy: #232755;
    --paper: #f7f7f5;
    --backdrop: #e4e4e4;
    --ink: #2b2b2b;
    --hard-1: #f1df85;
    --hard-2: #f4b41a;
    --hard-3: #ec7a1c;
    --hard-4: #d61f1f;
  }
  * { box-sizing: border-box; margin: 0; padding: 0; }
  html, body { width: 1200px; height: 847px; overflow: hidden; }
  body {
    background: var(--backdrop);
    display: flex; align-items: center; justify-content: center;
    font-family: "Open Sans", Arial, sans-serif;
  }
  .spread {
    display: flex;
    width: 1080px; height: 764px;
    box-shadow: 0 10px 30px rgba(0,0,0,0.18);
  }
  .page { width: 540px; height: 764px; position: relative; overflow: hidden; }

  /* Left page */
  .page--problems {
    background: linear-gradient(90deg, var(--paper) 88%, #e6e6e3 100%);
    padding: 70px 48px 0 58px;
    color: var(--ink);
  }
  .page-title {
    font-family: "Montserrat", Arial, sans-serif;
    font-weight: 300; font-size: 36px; letter-spacing: -0.5px;
  }
  .page--problems .page-title { color: var(--brand-red); }
  .page-subtitle {
    font-family: "Arimo", Arial, sans-serif;
    font-weight: 700; font-size: 15.5px; color: var(--brand-blue);
    margin: 6px 0 18px;
  }
  .body-copy { font-size: 9.5px; line-height: 1.45; margin-bottom: 10px; color: #333; }
  .hardness-legend { list-style: none; margin: 22px 0 22px 34px; }
  .hardness-legend li {
    display: flex; align-items: center; gap: 10px;
    font-family: "Arimo", Arial, sans-serif; font-size: 15px; margin-bottom: 4px;
  }
  .hardness-legend strong { font-weight: 700; }
  .swatch { width: 16px; height: 16px; border: 1px solid #555; flex: none; }
  .swatch--slight { background: var(--hard-1); }
  .swatch--moderate { background: var(--hard-2); }
  .swatch--hard { background: var(--hard-3); }
  .swatch--very { background: var(--hard-4); }
  .hardness-map {
    width: 410px; height: 250px; margin-left: 26px;
    border-radius: 40px 70px 30px 90px;
    background: radial-gradient(ellipse at 38% 50%, var(--hard-4) 0%, var(--hard-3) 35%, var(--hard-2) 60%, var(--hard-1) 85%);
  }

  /* Right page */
  .page--effects {
    background: linear-gradient(90deg, var(--brand-red-dark) 0%, var(--brand-red) 30%, var(--brand-red-deep) 100%);
    color: #fff;
    padding: 70px 60px 0 40px;
  }
  .effects-photo {
    position: absolute; right: 0; top: 170px; width: 300px; height: 520px;
    background: radial-gradient(ellipse at 55% 35%, #d65a5a 0%, #b82a2e 45%, rgba(169,27,34,0) 75%);
  }
  .page--effects .page-title { color: #fff; position: relative; }
  .effects-intro { font-size: 10px; font-weight: 700; margin: 14px 0 8px; position: relative; }
  .effects-list { list-style: disc; padding-left: 28px; position: relative; max-width: 330px; }
  .effects-list li { font-size: 9.5px; line-height: 1.42; margin-bottom: 2px; }
</style>
</head>
<body>
  <main class="spread">
    <section class="page page--problems">
      <h1 class="page-title">Hard Water Problems</h1>
      <h2 class="page-subtitle">What makes the water in Tucson and Southern Arizona so hard?</h2>
      <p class="body-copy">As you can see from the map below, Tucson sits right at the bottom of a band of very hard water, i.e. a high level of calcium, magnesium, iron and other minerals in the water. Because our water travels so far, from the Rockies down through Nevada and then through most of Arizona, it tends to absorb a high level of those minerals on its journey.</p>
      <p class="body-copy">It's clear that here in Southern Arizona, we need a whole house water softening system even more than in most other areas of the country.</p>
      <ul class="hardness-legend">
        <li><span class="swatch swatch--slight"></span><span><strong>Slightly Hard Water</strong> (1 - 3.5 Grains Per Gallon)</span></li>
        <li><span class="swatch swatch--moderate"></span><span><strong>Moderately Hard Water</strong> (3.5 - 7 Grains Per Gallon)</span></li>
        <li><span class="swatch swatch--hard"></span><span><strong>Hard Water</strong> (7 - 10.5 Grains Per Gallon)</span></li>
        <li><span class="swatch swatch--very"></span><span><strong>Very Hard Water</strong> (10.5+ Grains Per Gallon)</span></li>
      </ul>
      <div class="hardness-map" role="img" aria-label="Map of the United States shaded by water hardness, darkest red across the Southwest and Mountain states"></div>
    </section>

    <section class="page page--effects">
      <div class="effects-photo" role="img" aria-label="Red-toned photograph of cupped hands holding water"></div>
      <h1 class="page-title">Effects Of Hard Water</h1>
      <p class="effects-intro">Hard water has a number of negative effects on Arizona home owners:</p>
      <ul class="effects-list">
        <li>Water smells and tastes metallic or moldy, and can look cloudy.</li>
        <li>Minerals clog up pipes like plaque in arteries, reducing flow and increasing chances of expensive and damaging pipe leaks.</li>
        <li>Minerals clog home appliances such as refrigerators, ice machines, washing machines and dishwashers, making them work harder. This increases energy usage and reduces lifespan of the appliance. Hard water also erodes rubber seals, making an expensive and stressful leak more likely to occur.</li>
        <li>Hard water is damaging to your water heater's heating element, again increasing energy usage and reducing lifespan.</li>
        <li>Iron causes dirty looking reddish brown stains on porcelain.</li>
        <li>Calcium causes white water spots on dishes, cutlery, sinks and countertops, making constant clean up necessary. On shower curtains this can create a microbial biofilm containing disease spreading bacteria.</li>
        <li>Minerals deactivate the active ingredients in soap and detergent. This makes it hard to get a good lather in the shower, and difficult to wash soap properly off the body, leading to dry skin and difficult to manage hair. This is even more difficult when calcium clogs your showerhead, reducing pressure.</li>
        <li>Soap on the body all day can also exacerbate eczema, especially in children.</li>
        <li>Clothes don't get fully clean, and residual soap on laundry allows even more dirty and grime to stick to it. Fibers wear out faster and since more detergent and hotter water is needed, clothes tend to fade faster in homes with hard water.</li>
        <li>The National Water Quality Council estimates hard water reduces washing machine lifespan by 30%, and costs the average homeowner over $800 per year.</li>
      </ul>
    </section>
  </main>
</body>
</html>
```